Stationery Design Project

We are looking for a full revision of our existing stationary to include within this project:

- Letterhead
- Business card
- Compliment slip

The items should be a reflection of our new website which can be found at http://www.larkfieldchecks.co.uk/

Our logo files are included within the file brief

There are some further projects which we may approach the winning designer for as we need a revision to the front cover of our reports, a new price list and two brochures for specific target markets.

Industry/Entity Type

Business

```html
<!DOCTYPE html>
<html lang="en">
<head>
<meta charset="utf-8">
<title>Larkfield Checks – Stationery</title>
<link href="https://fonts.googleapis.com/css2?family=Source+Sans+3:ital,wght@0,400;0,600;0,700;1,400&family=Roboto+Condensed:wght@700&display=swap" rel="stylesheet">
<style>
  :root {
    --backdrop: #222222;
    --paper: #ffffff;
    --navy: #0c0f66;
    --navy-deep: #07094a;
    --royal: #1446a8;
    --sky: #7fc8ff;
    --card-top: #1e1c5e;
    --card-bottom: #000000;
    --muted: #d6d6e6;
  }
  * { box-sizing: border-box; margin: 0; padding: 0; }
  html, body { width: 1200px; height: 1000px; overflow: hidden; background: var(--backdrop); }
  body { position: relative; font-family: "Source Sans 3", "Myriad Pro", sans-serif; }

  .letterhead {
    position: absolute; left: 69px; top: 34px; width: 690px; height: 894px;
    background: var(--paper); overflow: hidden;
    box-shadow: 0 2px 8px rgba(0,0,0,.5);
  }
  .letterhead__topband { position: absolute; left: 0; top: 0; width: 100%; height: 14px; background: var(--navy); border-bottom: 4px solid var(--royal); }
  .letterhead__brand { position: absolute; left: 15px; top: 42px; font-size: 25px; }
  .letterhead__waves { position: absolute; left: 0; bottom: 0; width: 690px; height: 135px; display: block; }
  .letterhead__footer {
    position: absolute; right: 11px; bottom: 11px; text-align: right;
    font-family: "Roboto Condensed", "Helvetica Neue", sans-serif; font-weight: 700;
    font-size: 8.5px; line-height: 12px; color: var(--muted);
  }
  .letterhead__footer .footer-name { color: var(--paper); }

  .brand-name { font-weight: 700; color: var(--navy); letter-spacing: .02em; white-space: nowrap; line-height: 1; }

  .card { position: absolute; left: 626px; width: 439px; height: 262px; background: var(--paper); overflow: hidden; box-shadow: 0 3px 10px rgba(0,0,0,.55); }
  .card--front { top: 232px; }
  .card--front .brand-name { position: absolute; left: 0; right: 0; top: 112px; text-align: center; font-size: 40px; }
  .card--back { top: 528px; }
  .card__panel { position: absolute; inset: 0; width: 439px; height: 262px; display: block; }
  .card__contact { position: absolute; color: var(--paper); }
  .card__person { right: 217px; top: 44px; text-align: right; }
  .card__person .person-name { font-weight: 700; font-size: 14.5px; line-height: 18px; }
  .card__person .person-email { color: var(--sky); font-size: 12px; line-height: 16px; }
  .card__person .person-mobile { color: var(--muted); font-size: 12px; line-height: 16px; }
  .card__address { right: 217px; top: 112px; text-align: right; font-size: 10px; line-height: 13.5px; }
  .card__lines { left: 253px; top: 112px; font-size: 10px; line-height: 13.5px; }
  .card__lines .site { color: var(--sky); font-style: italic; }
  .card--back .brand-name { position: absolute; right: 24px; top: 210px; font-size: 20px; }
</style>
</head>
<body>

<section class="letterhead" aria-label="Letterhead">
  <div class="letterhead__topband"></div>
  <div class="letterhead__brand brand-name">LARKFIELD CHECKS</div>
  <svg class="letterhead__waves" viewBox="0 0 690 135" aria-hidden="true">
    <path d="M0,0 Q345,112 690,36 L690,135 L0,135 Z" fill="var(--royal)"/>
    <path d="M0,17 Q345,126 690,50 L690,135 L0,135 Z" fill="var(--navy)"/>
    <path d="M582,31 Q632,10 690,3 L690,12 Q640,16 582,31 Z" fill="var(--royal)"/>
  </svg>
  <div class="letterhead__footer">
    <div class="footer-name">LARKFIELD CHECKS</div>
    <div>Office Address: 48 Orchard Row, Maidstone Kent</div>
    <div>Office Number: 415 284 3170</div>
  </div>
</section>

<section class="card card--front" aria-label="Business card front">
  <div class="brand-name">LARKFIELD CHECKS</div>
</section>

<section class="card card--back" aria-label="Business card back">
  <svg class="card__panel" viewBox="0 0 439 262" aria-hidden="true">
    <defs>
      <linearGradient id="cardShade" x1="0" y1="0" x2="0" y2="1">
        <stop offset="0" stop-color="var(--card-top)"/>
        <stop offset="0.4" stop-color="var(--card-top)"/>
        <stop offset="1" stop-color="var(--card-bottom)"/>
      </linearGradient>
    </defs>
    <path d="M0,0 H439 V118 Q380,200 0,215 Z" fill="url(#cardShade)"/>
    <path d="M439,118 Q380,200 0,215" fill="none" stroke="var(--royal)" stroke-width="3"/>
  </svg>
  <div class="card__contact card__person">
    <div class="person-name">Tom Harlow</div>
    <div class="person-email">harlow.tom@larkfieldchecks.com</div>
    <div class="person-mobile">Mobile: +415 2611 408</div>
  </div>
  <div class="card__contact card__address">
    <div>48 Orchard Row</div>
    <div>District Name</div>
    <div>City Name City</div>
    <div>2153</div>
  </div>
  <div class="card__contact card__lines">
    <div>Phone: +415 2377 904</div>
    <div>Fax: +415 238 51 60</div>
    <div class="site">www.larkfieldchecks.com</div>
  </div>
  <div class="brand-name">LARKFIELD CHECKS</div>
</section>

</body>
</html>
```